Cardboard hanging box designs

I need to get some cardboard boxes made up for trailer wheel bearing kits. They need to be hanging boxes as pictured. The box needs to fit with our existing colour scheme and be clearly evident that it is for trailers. I am after 2 designs, one for "Trailer Bearing Kit" and one for "Marine Bearing Kit".
The Marine Bearing kit box should measure, 180mm High, 120mm Wide, 60mm Deep.
The Trailer Bearing kit box should measure, 180mm high, 120mm Wide, 30mm Deep.
These are all external measurements.

```html
<!DOCTYPE html>
<html lang="en">
<head>
<meta charset="utf-8">
<title>Bearing Kit Hanging Boxes</title>
<link rel="stylesheet" href="https://fonts.googleapis.com/css2?family=Audiowide&family=Roboto+Condensed:wght@400&family=Montserrat:wght@500&display=swap">
<style>
  :root {
    --trailer: #d0263a;
    --trailer-bright: #e0384a;
    --marine: #22a3d6;
    --marine-bright: #20aee3;
    --yellow: #eddc3c;
    --body-dark: #121112;
    --body-mid: #262326;
    --paper: #ffffff;
    --type-white: #f4f4f4;
  }
  html, body {
    margin: 0;
    padding: 0;
    width: 1200px;
    height: 960px;
    overflow: hidden;
    background: var(--paper);
  }
  .canvas {
    position: relative;
    width: 1200px;
    height: 960px;
  }
  .box {
    position: absolute;
    top: 54px;
    width: 426px;
    height: 804px;
  }
  .box--trailer { left: 144px; --accent: var(--trailer); --accent-bright: var(--trailer-bright); }
  .box--marine  { left: 630px; --accent: var(--marine);  --accent-bright: var(--marine-bright); }

  .hanger {
    position: absolute;
    left: 3px;
    top: 0;
    width: 420px;
    height: 129px;
    background: var(--accent);
  }
  .hanger__hole {
    position: absolute;
    left: 140px;
    top: 42px;
    width: 138px;
    height: 36px;
  }
  .hanger__brand {
    position: absolute;
    left: 8px;
    top: 60px;
    transform: rotate(90deg);
    transform-origin: left top;
    font-family: "Audiowide", sans-serif;
    font-size: 17px;
    color: var(--yellow);
    white-space: nowrap;
    margin-left: 20px;
  }

  .front {
    position: absolute;
    left: 0;
    top: 129px;
    width: 426px;
    height: 675px;
    background: linear-gradient(180deg, var(--body-dark) 0%, var(--body-mid) 100%);
    overflow: hidden;
  }
  .front__stripes {
    position: absolute;
    inset: 0;
    width: 426px;
    height: 675px;
  }
  .title {
    position: absolute;
    left: 0;
    width: 426px;
    top: 38px;
    text-align: center;
    font-family: "Audiowide", sans-serif;
    line-height: 1;
    margin: 0;
  }
  .title__kind {
    display: block;
    font-size: 32px;
    color: var(--accent);
  }
  .title__product {
    display: block;
    font-size: 28px;
    color: var(--yellow);
    margin-top: 0;
    letter-spacing: 1px;
  }
  .product-photo {
    position: absolute;
    left: 60px;
    top: 108px;
    width: 306px;
    height: 390px;
    border-radius: 50%;
    background: radial-gradient(ellipse at 50% 45%, #9a9a9a 0%, #5a595a 35%, #2a282a 65%, rgba(30,28,30,0) 75%);
  }
  .brand {
    position: absolute;
    left: 26px;
    top: 509px;
    font-family: "Audiowide", sans-serif;
    font-size: 26px;
    color: var(--yellow);
    margin: 0;
  }
  .benefits {
    position: absolute;
    left: 24px;
    top: 552px;
    margin: 0;
    padding: 0;
    list-style: none;
    font-family: "Roboto Condensed", sans-serif;
    font-size: 17px;
    line-height: 20.6px;
    color: var(--accent-bright);
  }
  .benefits li {
    position: relative;
    padding-left: 12px;
  }
  .benefits li::before {
    content: "";
    position: absolute;
    left: 0;
    top: 7px;
    width: 6px;
    height: 6px;
    background: var(--yellow);
  }
  .web {
    position: absolute;
    left: 222px;
    top: 625px;
    font-family: "Montserrat", sans-serif;
    font-weight: 500;
    font-size: 13px;
    letter-spacing: 1.6px;
    color: var(--type-white);
  }
</style>
</head>
<body>
<main class="canvas">

  <section class="box box--trailer">
    <div class="hanger">
      <svg class="hanger__hole" viewBox="0 0 138 36" aria-hidden="true">
        <path d="M14 9 H52 C60 9 62 0 69 0 C76 0 78 9 86 9 H124 A13 13 0 0 1 124 35 H14 A13 13 0 0 1 14 9 Z" fill="#ffffff"/>
      </svg>
      <span class="hanger__brand">KVR</span>
    </div>
    <div class="front">
      <svg class="front__stripes" viewBox="0 0 710 1125" preserveAspectRatio="none" aria-hidden="true">
        <polygon points="0,580 0,612 282,743" fill="var(--trailer-bright)"/>
        <polygon points="0,645 0,705 410,823" fill="var(--yellow)"/>
        <polygon points="215,827 710,960 710,1067" fill="var(--trailer-bright)"/>
        <polygon points="595,1032 710,1090 710,1112" fill="var(--yellow)"/>
      </svg>
      <h1 class="title">
        <span class="title__kind">TRAILER</span>
        <span class="title__product">BEARING KIT</span>
      </h1>
      <div class="product-photo" role="img" aria-label="Photo of tapered roller bearings, races, grease seal, washer and cotter pin"></div>
      <p class="brand">KVR PARTS</p>
      <ul class="benefits">
        <li>Miximum Load Carring Capacity</li>
        <li>Ultimate Protection</li>
        <li>Increased Reliability</li>
        <li>Longer Life</li>
      </ul>
      <span class="web">www.kvrparts.com</span>
    </div>
  </section>

  <section class="box box--marine">
    <div class="hanger">
      <svg class="hanger__hole" viewBox="0 0 138 36" aria-hidden="true">
        <path d="M14 9 H52 C60 9 62 0 69 0 C76 0 78 9 86 9 H124 A13 13 0 0 1 124 35 H14 A13 13 0 0 1 14 9 Z" fill="#ffffff"/>
      </svg>
      <span class="hanger__brand">KVR</span>
    </div>
    <div class="front">
      <svg class="front__stripes" viewBox="0 0 710 1125" preserveAspectRatio="none" aria-hidden="true">
        <polygon points="0,580 0,612 282,743" fill="var(--marine-bright)"/>
        <polygon points="0,645 0,705 410,823" fill="var(--yellow)"/>
        <polygon points="215,827 710,960 710,1067" fill="var(--marine-bright)"/>
        <polygon points="595,1032 710,1090 710,1112" fill="var(--yellow)"/>
      </svg>
      <h1 class="title">
        <span class="title__kind">MARINE</span>
        <span class="title__product">BEARING KIT</span>
      </h1>
      <div class="product-photo" role="img" aria-label="Photo of tapered roller bearings, races, grease seal, washer and cotter pin"></div>
      <p class="brand">KVR PARTS</p>
      <ul class="benefits">
        <li>Miximum Load Carring Capacity</li>
        <li>Ultimate Protection</li>
        <li>Increased Reliability</li>
        <li>Longer Life</li>
      </ul>
      <span class="web">www.kvrparts.com</span>
    </div>
  </section>

</main>
</body>
</html>
```